Business Card Design

We need a business card design that can also be aplied for postcards. We are a small indie record company that also do consulting, and development of independat artitst . I already have the name and the basic idea of what i am looking for but i am open to any suggestion.
Info for the card
Name of the company : Velmora Records
NAME : Tobias Lindqvist
PHONE : 314-5820641
EMAIL : hello@velmorarecords.example
WEB: www.velmorarecords.example
Target Market(s)
Male - Female independent musicians ages 18 to 45
Industry/Entity Type
Record Company
Contact Information for Business Card
Independant records company that also works in consulting for music business models for independent artists
Look and feel

```html
<!DOCTYPE html>
<html lang="en">
<head>
<meta charset="utf-8">
<title>Velmora Records – Business Card</title>
<link href="https://fonts.googleapis.com/css2?family=Questrial&family=Kaushan+Script&display=swap" rel="stylesheet">
<style>
  :root {
    --backdrop: #ececec;
    --card-blue: #0aa6e6;
    --card-blue-deep: #0d5f86;
    --card-blue-light: #7fd3f5;
    --splash-red: #cf2232;
    --splash-yellow: #ffee00;
    --splash-white: #ffffff;
    --name-yellow: #fff200;
    --ink-white: #ffffff;
  }
  html, body {
    margin: 0;
    width: 1200px;
    height: 940px;
    overflow: hidden;
    background: var(--backdrop);
  }
  .canvas {
    position: relative;
    width: 1200px;
    height: 940px;
  }
  .card {
    position: absolute;
    width: 640px;
    height: 380px;
    overflow: hidden;
    box-shadow: 0 6px 18px rgba(0,0,0,0.25);
  }
  /* Front of card */
  .card-front {
    left: 140px;
    top: 130px;
    z-index: 2;
    background: radial-gradient(ellipse at 55% 55%, var(--card-blue) 0%, #0b8cc4 55%, var(--card-blue-deep) 100%);
  }
  .paint-splash {
    position: absolute;
    inset: 0;
    background:
      radial-gradient(ellipse 150px 120px at 88% 18%, rgba(255,238,0,0.95), rgba(255,238,0,0) 100%),
      radial-gradient(ellipse 200px 110px at 48% 55%, rgba(207,34,50,0.9), rgba(207,34,50,0) 100%),
      radial-gradient(ellipse 150px 120px at 12% 85%, rgba(255,255,255,0.85), rgba(255,255,255,0) 100%);
  }
  .brand-name {
    position: absolute;
    left: 70px;
    top: 62px;
    margin: 0;
    font-family: "Questrial", sans-serif;
    font-weight: 400;
    font-size: 54px;
    line-height: 54px;
    color: var(--ink-white);
  }
  /* Back of card */
  .card-back {
    left: 470px;
    top: 495px;
    z-index: 1;
    background: var(--card-blue);
  }
  .faint-splash {
    position: absolute;
    inset: 0;
    background:
      radial-gradient(ellipse 170px 150px at 10% 75%, rgba(127,211,245,0.8), rgba(127,211,245,0) 100%),
      radial-gradient(ellipse 110px 150px at 82% 25%, rgba(127,211,245,0.7), rgba(127,211,245,0) 100%);
  }
  .holder-name {
    position: absolute;
    left: 90px;
    top: 10px;
    margin: 0;
    font-family: "Kaushan Script", cursive;
    font-size: 44px;
    color: var(--name-yellow);
  }
  .contact-list {
    position: absolute;
    left: 245px;
    top: 155px;
    margin: 0;
    padding: 0;
    list-style: none;
    font-family: "Questrial", sans-serif;
    font-size: 22px;
    line-height: 26px;
    font-weight: 700;
    color: var(--ink-white);
  }
</style>
</head>
<body>
  <main class="canvas">
    <section class="card card-front">
      <div class="paint-splash" role="img" aria-label="Splashes of yellow, red and white paint across the blue card"></div>
      <h1 class="brand-name">Velmora<br>Records</h1>
    </section>

    <section class="card card-back">
      <div class="faint-splash" role="img" aria-label="Faint light blue paint splashes"></div>
      <h2 class="holder-name">Tobias Lindqvist</h2>
      <ul class="contact-list">
        <li class="contact-phone">314-5820641</li>
        <li class="contact-email">hello@velmorarecords.example</li>
        <li class="contact-web">www.velmorarecords.example</li>
      </ul>
    </section>
  </main>
</body>
</html>
```